New Branding Business Card Design

Redesign business card according to new branding update.

** The design received so far are single color + BLACK.
I'd encourage designer to use different tones of blue / purple as described in the Designer Brief color palette

Target Market(s)

International

Industry/Entity Type

Medical Equipment

Contact Information for Business Card

Logo on one side (Designer can decide if they want to move certain info from the other side to save space)

Main body info (company name, individual name in both English and Chinese, contact info etc) on the other
Prefer a 'cleaner' layout - vs 'all over the place'
Prefer flush left alignment

Font styles to use
Sans Serif

Requirements
Must have
• Key info
• (Company name (English)): VORAM (HK) Limited
• (Name (English)): Marcus L. Pryde
• (Credential): FCPA, FHKSI
• (Title): Founder, Managing Director & CEO
• For the following info, designers decide whether to use colon or no colon, stroke separator, or use icon gfx for T (for telephone fixed line, M for mobile etc.)
• T: +852 3517 VORAM / +852 3517 4062
• M: +852 6243 7719 / + 86 139 2745 3186
• E: marcus.l.pryde@voram-example.hk
Nice to have
• Depending on the space and spacing available designers can add or use fuller title and other info
• Title: Chairman of the Executive Committee, Founder, Managing Director & CEO
• (Name (Chinese)): 林書恒
Should not have
• One of our business entities a long company name that cannot be broken into 2 lines
• makes vertical implementation almost impossible

```html
<!DOCTYPE html>
<html lang="en">
<head>
<meta charset="utf-8">
<title>VORAM (HK) Limited – Business Card</title>
<link rel="stylesheet" href="https://fonts.googleapis.com/css2?family=Figtree:wght@400;600;700;800&family=Noto+Sans+TC:wght@500&display=swap">
<style>
  :root {
    --stage: #000000;
    --card: #e9e9e9;
    --brand-purple: #5a2a7f;
    --brand-violet: #4a3a9c;
    --brand-blue: #2f4f9e;
    --ink: #1b1b1b;
  }
  * { box-sizing: border-box; margin: 0; padding: 0; }
  html, body {
    width: 1200px; height: 1200px; overflow: hidden;
    background: var(--stage);
    font-family: "Figtree", "Helvetica Neue", Arial, sans-serif;
  }
  .stage { position: relative; width: 1200px; height: 1200px; }
  .card {
    position: absolute; left: 146px; width: 908px; height: 517px;
    background: var(--card); border-radius: 54px;
  }
  .card--front { top: 56px; }
  .card--back { top: 628px; }

  .wordmark {
    position: absolute; display: flex; align-items: center; gap: 18px;
    color: var(--brand-purple); font-weight: 800; letter-spacing: 0.04em;
  }
  .wordmark__square {
    background: var(--brand-blue); border-radius: 10px; flex: none;
  }
  .card--front .wordmark {
    left: 0; right: 0; top: 0; bottom: 0; justify-content: center; font-size: 84px;
  }
  .card--front .wordmark__square { width: 70px; height: 70px; border-radius: 14px; }
  .card--back .wordmark {
    right: 50px; top: 117px; height: 284px; font-size: 50px; gap: 12px;
  }
  .card--back .wordmark__square { width: 42px; height: 42px; }

  .details { position: absolute; left: 48px; top: 102px; color: var(--ink); }
  .details__name {
    color: var(--brand-purple); font-weight: 800; font-size: 37px;
    letter-spacing: -0.02em; line-height: 1; white-space: nowrap;
  }
  .details__name-zh {
    font-family: "Noto Sans TC", sans-serif; font-weight: 500;
    font-size: 30px; letter-spacing: 0.04em; margin-left: 6px;
  }
  .details__title { margin-top: 8px; font-weight: 600; font-size: 16.5px; line-height: 22px; }
  .details__credentials { color: var(--brand-blue); font-weight: 700; margin-left: 10px; }
  .details__company {
    margin-top: 27px; color: var(--brand-violet); font-weight: 700; font-size: 20px; line-height: 22px;
  }
  .details__address { font-size: 21px; line-height: 22px; margin-top: 4px; }
  .contact { margin-top: 20px; font-size: 20px; line-height: 24px; }
  .contact + .contact { margin-top: 10px; }
  .contact__label { color: var(--brand-blue); font-weight: 700; font-size: 20px; }
  .contact--email { margin-top: 12px; }
</style>
</head>
<body>
<main class="stage">
  <section class="card card--front" aria-label="Card front">
    <div class="wordmark"><span class="wordmark__square"></span>VORAM</div>
  </section>

  <section class="card card--back" aria-label="Card back">
    <div class="details">
      <h1 class="details__name">MARCUS L. PRYDE<span class="details__name-zh">林書恒</span></h1>
      <p class="details__title">Chairman of the Executive Committee, Founder<br>Managing Director &amp; CEO<span class="details__credentials">FCPA, FHKSI</span></p>
      <p class="details__company">VORAM (HK) Limited</p>
      <p class="details__address">2nd Floor, Larchmont Tower<br>18-22 Fernleigh Lane, Central, Hong Kong</p>
      <p class="contact"><span class="contact__label">Telephone:</span><br>+ 852 3517 VORAM / + 852 3517 4062</p>
      <p class="contact"><span class="contact__label">Mobile:</span><br>+ 852 6243 7719 / + 86 139 2745 3186</p>
      <p class="contact contact--email"><span class="contact__label">Email:</span> marcus.l.pryde@voram-example.hk</p>
    </div>
    <div class="wordmark"><span class="wordmark__square"></span>VORAM</div>
  </section>
</main>
</body>
</html>
```